Meadowlark Learning Growth Partners (MLGP)

This is a professional business card. Logo and picture are a must on the front of the card. I am an educational consultant. I have been consulting for the past three years for a company. I am now opening my own company. My goal for my consulting company is to eventually consult all over America.

Target Market(s)

Educators, schools, professionals

Industry/Entity Type

Consulting

Contact Information for Business Card

Picture/logo on front, simple modern design

Font styles to use
Serif

Colors
85abd2
0355a3
3176b5
cedeed

Requirements
Must have
• picture, logo,
• Odessa Pruitt, Ed.S
• address 5073 Cormorant ridge Dr. Nashville, TN 37940
• Cell:616-555-0148
• Office: 629-555-0172
• www.Mlgpedu.example
• pruittodessa@mailbox.example

```html
<!DOCTYPE html>
<html lang="en">
<head>
<meta charset="utf-8">
<title>Meadowlark Learning Growth Partners — Business Card</title>
<link rel="stylesheet" href="https://fonts.googleapis.com/css2?family=Lexend:wght@600;700&family=Arimo:wght@400;700&display=swap">
<style>
  :root {
    --page: #e8e5e0;
    --navy: #1c3f88;
    --brand: #163f8c;
    --royal: #2a55b0;
    --bright: #2f5fc4;
    --light-tri: #5a7fc8;
    --white: #ffffff;
    --back-hi: #0f58ad;
    --back-lo: #023a8a;
    --photo-a: #c9ccd3;
    --photo-b: #2b2f3a;
  }
  * { margin: 0; padding: 0; box-sizing: border-box; }
  html, body { width: 900px; height: 1200px; overflow: hidden; }
  body { background: var(--page); position: relative; font-family: "Arimo", Arial, sans-serif; }

  .card {
    position: absolute; left: 85px; width: 725px; height: 423px; overflow: hidden;
    box-shadow: 0 6px 14px rgba(0,0,0,0.25);
  }
  .card--front { top: 157px; background: var(--white); }
  .card--back {
    top: 634px;
    background: radial-gradient(circle at 35% 25%, var(--back-hi) 0%, var(--back-lo) 90%);
  }

  .front-shapes { position: absolute; inset: 0; }

  .brand { position: absolute; display: flex; align-items: center; font-family: "Lexend", sans-serif; font-weight: 700; }
  .brand__mark { width: 62px; height: 62px; border-radius: 50%; margin-right: 16px; }
  .brand__short { font-size: 36px; letter-spacing: 2px; margin-right: 16px; }
  .brand__divider { width: 2px; align-self: stretch; margin-right: 14px; }
  .brand__name { font-size: 19px; line-height: 25px; }

  .card--front .brand { left: 55px; top: 40px; height: 100px; color: var(--brand); }
  .card--front .brand__mark { background: var(--brand); }
  .card--front .brand__divider { background: var(--brand); }

  .card--back .brand { left: 135px; top: 158px; height: 108px; color: var(--white); }
  .card--back .brand__mark { background: var(--white); width: 70px; height: 70px; }
  .card--back .brand__short { font-size: 38px; }
  .card--back .brand__divider { background: var(--white); }
  .card--back .brand__name { font-size: 21px; line-height: 28px; }

  .holder-name {
    position: absolute; left: 45px; top: 193px;
    font-family: "Arimo", Arial, sans-serif; font-weight: 700; font-size: 22px;
    color: var(--white); letter-spacing: 0.3px;
  }

  .contact-list { position: absolute; left: 46px; top: 262px; list-style: none; color: var(--white); font-size: 16.5px; }
  .contact-list li { display: flex; align-items: center; height: 27.8px; }
  .contact-list svg { width: 16px; height: 16px; margin-right: 11px; fill: var(--white); flex: none; }

  .portrait {
    position: absolute; left: 430px; top: 28px; width: 295px; height: 395px;
    background: linear-gradient(180deg, var(--photo-a) 0%, #9aa0ab 45%, var(--photo-b) 100%);
  }
</style>
</head>
<body>

<section class="card card--front" aria-label="Business card front">
  <svg class="front-shapes" viewBox="0 0 725 423" width="725" height="423" aria-hidden="true">
    <rect x="0" y="233" width="725" height="190" fill="var(--royal)"/>
    <polygon points="725,28 725,233 440,233" fill="var(--bright)"/>
    <rect x="0" y="180" width="500" height="53" fill="var(--navy)"/>
    <polygon points="400,180 470,180 430,230" fill="var(--light-tri)" opacity="0.7"/>
    <polyline points="0,278 44,236 500,236" fill="none" stroke="var(--white)" stroke-width="4"/>
  </svg>

  <div class="brand">
    <span class="brand__mark"></span>
    <span class="brand__short">MLGP</span>
    <span class="brand__divider"></span>
    <span class="brand__name">Meadowlark<br>Learning<br>Growth<br>Partners</span>
  </div>

  <div class="holder-name">ODESSA PRUITT, ED.S</div>

  <ul class="contact-list">
    <li><svg viewBox="0 0 16 16"><path d="M4 0h8a1 1 0 0 1 1 1v14a1 1 0 0 1-1 1H4a1 1 0 0 1-1-1V1a1 1 0 0 1 1-1zm1 2v10h6V2zm3 11a1 1 0 1 0 0 2 1 1 0 0 0 0-2z"/></svg>616-555-0148</li>
    <li><svg viewBox="0 0 16 16"><path d="M1 5c0-2 3-3 7-3s7 1 7 3v1h-4V4.5H5V6H1zm3 2h8l3 4v3H1v-3zm4 1.5a2 2 0 1 0 0 4 2 2 0 0 0 0-4z"/></svg>629-555-0172</li>
    <li><svg viewBox="0 0 16 16"><path d="M8 0a8 8 0 1 0 0 16A8 8 0 0 0 8 0zm0 1.5c1 0 2 2 2.3 5.5H5.7C6 3.5 7 1.5 8 1.5zM1.6 8.5h2.6c.1 2 .5 3.8 1.1 5A6.5 6.5 0 0 1 1.6 8.5zm0-1.5a6.5 6.5 0 0 1 3.7-4.5c-.6 1.2-1 2.6-1.1 4.5zm4.1 1.5h4.6c-.3 3.5-1.3 6-2.3 6s-2-2.5-2.3-6zm5 5c.6-1.2 1-3 1.1-5h2.6a6.5 6.5 0 0 1-3.7 5zm1.1-6.5c-.1-1.9-.5-3.3-1.1-4.5A6.5 6.5 0 0 1 14.4 7z"/></svg>www.Mlgpedu.example</li>
    <li><svg viewBox="0 0 16 16"><path d="M0 3h16v1.2L8 9 0 4.2zm0 2.6 8 4.8 8-4.8V13H0z"/></svg>pruittodessa@mailbox.example</li>
    <li><svg viewBox="0 0 16 16"><path d="M8 0a5.5 5.5 0 0 0-5.5 5.5C2.5 10 8 16 8 16s5.5-6 5.5-10.5A5.5 5.5 0 0 0 8 0zm0 3a2.5 2.5 0 1 1 0 5 2.5 2.5 0 0 1 0-5z"/></svg>5073 Cormorant ridge Dr. Nashville, TN 37940</li>
  </ul>

  <div class="portrait" role="img" aria-label="Portrait photograph of Odessa Pruitt in a dark blazer and white blouse"></div>
</section>

<section class="card card--back" aria-label="Business card back">
  <div class="brand">
    <span class="brand__mark"></span>
    <span class="brand__short">MLGP</span>
    <span class="brand__divider"></span>
    <span class="brand__name">Meadowlark<br>Learning<br>Growth<br>Partners</span>
  </div>
</section>

</body>
</html>
```